Statement on the current financial and economic crisis, with a focus on Greece,

Anybody can become angry - that is easy, but to be angry with the right person and to the right degree and at the right time and for the right purpose, and in the right way - that is not within everybody's power and is not easy.
(Kelphinor ) greek philosopher

i want to do a poster with this words from Kelphinor greek philosopher and to show this statement for the greek people... its about for my project that i am doing.

Target Market(s)

my audience will be greek people but not only, from 18-80 years old for that reason i want my statement to be in english.

Industry/Entity Type

Financial

Requirements
Must have
• Anybody can become angry - that is easy, but to be angry with the right person and to the right degree and at the right time and for the right purpose, and in the right way - that is not within everybody's power and is not easy.
i want to show in my poster this statement from:
Kelphinor greek philosopher (384 – 322 BC)

```html
<!DOCTYPE html>
<html lang="en">
<head>
<meta charset="utf-8">
<title>Kelphinor – Quote Poster</title>
<link href="https://fonts.googleapis.com/css2?family=Arvo:wght@700&family=Noticia+Text:wght@700&display=swap" rel="stylesheet">
<style>
  :root {
    --page: #ffffff;
    --poster-dark: #231f20;
    --poster-glow: #8a8a8a;
    --accent-blue: #00a8e8;
    --text-white: #ffffff;
    --bust-light: #bdbdbd;
    --bust-dark: #4a4a4a;
  }
  html, body {
    margin: 0;
    padding: 0;
    width: 900px;
    height: 1200px;
    overflow: hidden;
    background: var(--page);
  }
  .canvas {
    position: relative;
    width: 900px;
    height: 1200px;
  }
  .poster {
    position: absolute;
    left: 95px;
    top: 100px;
    width: 710px;
    height: 1002px;
    overflow: hidden;
    background:
      radial-gradient(ellipse 330px 300px at 385px 230px, var(--poster-glow) 0%, #4e4c4c 45%, var(--poster-dark) 100%);
  }
  .name-column {
    position: absolute;
    left: 62px;
    top: 62px;
    width: 150px;
    height: 640px;
    display: flex;
    align-items: center;
    justify-content: center;
  }
  .philosopher-name {
    margin: 0;
    writing-mode: vertical-rl;
    transform: rotate(180deg) scaleY(0.84);
    transform-origin: center;
    font-family: "Arvo", serif;
    font-weight: 700;
    font-size: 150px;
    line-height: 1;
    letter-spacing: -3px;
    color: var(--accent-blue);
    white-space: nowrap;
  }
  .philosopher-dates {
    position: absolute;
    left: 236px;
    top: 50px;
    height: 275px;
    margin: 0;
    writing-mode: vertical-rl;
    transform: rotate(180deg);
    font-family: "Noticia Text", serif;
    font-weight: 700;
    font-size: 15px;
    line-height: 1;
    color: var(--text-white);
    white-space: nowrap;
  }
  .quote-mark {
    position: absolute;
    font-family: "Noticia Text", serif;
    font-weight: 700;
    font-size: 240px;
    line-height: 1;
    color: var(--text-white);
  }
  .quote-mark--open { left: 313px; top: 32px; }
  .quote-mark--close { left: 535px; top: 830px; }
  .quote-text {
    position: absolute;
    left: 319px;
    top: 170px;
    margin: 0;
    font-family: "Noticia Text", serif;
    font-weight: 700;
    font-size: 31px;
    line-height: 52px;
    color: var(--text-white);
    white-space: nowrap;
  }
  .quote-text .highlight { color: var(--accent-blue); }
  .bust-portrait {
    position: absolute;
    left: 0;
    top: 740px;
    width: 318px;
    height: 262px;
    background:
      radial-gradient(ellipse 90px 110px at 155px 95px, var(--bust-light) 0%, #8e8e8e 60%, transparent 100%),
      radial-gradient(ellipse 200px 120px at 150px 262px, #cfcfcf 0%, var(--bust-dark) 75%, transparent 100%);
  }
</style>
</head>
<body>
  <div class="canvas">
    <section class="poster">
      <div class="name-column">
        <h1 class="philosopher-name">Kelphinor</h1>
      </div>
      <p class="philosopher-dates">Greek philosopher (384 – 322 BC)</p>
      <span class="quote-mark quote-mark--open" aria-hidden="true">“</span>
      <blockquote class="quote-text">
        Anybody can<br>
        become angry –<br>
        that is easy, but to<br>
        be angry with the<br>
        right person and<br>
        to the right degree<br>
        and at the right<br>
        time and for the<br>
        right purpose, and<br>
        in the right way –<br>
        <span class="highlight">that is not within<br>
        everybody's power<br>
        and is not easy.</span>
      </blockquote>
      <span class="quote-mark quote-mark--close" aria-hidden="true">”</span>
      <div class="bust-portrait" role="img" aria-label="Posterized grey-and-white photograph of a classical marble bust of the philosopher"></div>
    </section>
  </div>
</body>
</html>
```